Joomla Template Design

Wellvane.com is a web hosting company that serves the Christian church industry. We need a new template designed that we can offer our customers through our hosting interface.

The template needs to be designed in Joomla 2.5 or higher. If you can create it in Artisteer it's a plus, but not required.

The template should also include plug-ins for:

Photo / Video Gallery
Calender
Donations
Form Creator (for contact us type forms)
Site Search
Social Media Links

A general style sample is attached as a guide. The style should be clean and simple.

When the template is complete, it should be sent with 3 color palettes (blue, green, grey) and include all graphics.

Target Market(s)

This template will be used primarily for churches and ministries.

Industry/Entity Type

Church

Requirements
Must have
• The template must include home and interior page designs.
Nice to have
• We prefer the design be made with artisteer (see pagelume.com), but it's not required.

```html
<!DOCTYPE html>
<html lang="en">
<head>
<meta charset="utf-8">
<title>Wellvane Church Template – Colour Palettes</title>
<link rel="stylesheet" href="https://fonts.googleapis.com/css2?family=Noto+Serif:wght@400;700&display=swap">
<style>
:root{
  --canvas:#ffffff;
  --font:"Noto Serif", Georgia, serif;
}
.theme-blue{
  --frame:#6fa9cb; --sky-top:#f4f9fc; --sky-bottom:#bfdcea;
  --bar:#8fc0d6; --tab:#3c7391; --tab-text:#ffffff; --nav-text:#3c7391;
  --body:#ffffff; --mid:#dcedf5; --side:#eaf4f9; --rule:#cfe2ec;
  --heading:#6ea6c6; --text:#333333; --button:#4b89ab; --button-text:#ffffff;
  --link:#2c7099; --field:#ffffff; --field-line:#8aa9ba; --search:#ffffff;
}
.theme-grey{
  --frame:#444444; --sky-top:#f1f6f6; --sky-bottom:#a9c3c4;
  --bar:#777777; --tab:#9a9a9a; --tab-text:#222222; --nav-text:#bbbbbb;
  --body:#3b3b3b; --mid:#2f2f2f; --side:#343434; --rule:#555555;
  --heading:#9a9a9a; --text:#cfcfcf; --button:#7a7a7a; --button-text:#eeeeee;
  --link:#d6d6d6; --field:#3a3a3a; --field-line:#999999; --search:#2e2e2e;
}
.theme-green{
  --frame:#6f9c3c; --sky-top:#f6f9f0; --sky-bottom:#c9dbb3;
  --bar:#9cbd7a; --tab:#7cb342; --tab-text:#ffffff; --nav-text:#5d7a36;
  --body:#e9ede2; --mid:#dadfcd; --side:#e4e8da; --rule:#cdd3bd;
  --heading:#6f8f4c; --text:#333333; --button:#8fc35a; --button-text:#20300f;
  --link:#5b6b26; --field:#f3f5ee; --field-line:#a5ad93; --search:#f3f5ee;
}
*{box-sizing:border-box;margin:0;padding:0}
html,body{width:1200px;height:894px;overflow:hidden;background:var(--canvas)}
body{position:relative;font-family:var(--font);color:var(--text)}
.palette{position:absolute;width:592px;height:444px;overflow:hidden;border:2px solid var(--frame);background:var(--body)}
.palette--blue{left:6px;top:0}
.palette--grey{left:606px;top:0}
.palette--green{left:0;top:450px}

.masthead{position:absolute;left:0;top:0;width:100%;height:205px;background:linear-gradient(180deg,var(--sky-top),var(--sky-bottom))}
.masthead__photo{position:absolute;left:232px;top:8px;width:340px;height:173px;background:radial-gradient(ellipse at 50% 45%,#6d6a70 0%,#9ea3ad 35%,rgba(200,214,222,0) 72%)}
.brand{position:absolute;left:29px;top:64px;display:flex;align-items:center;gap:6px;font-size:20px;font-weight:700;color:#3d4d5a;letter-spacing:.5px}
.brand__mark{width:20px;height:20px;background:#2f7fc0}
.masthead__search{position:absolute;left:29px;top:154px;width:117px;height:13px;background:var(--search);border:1px solid var(--field-line)}
.nav{position:absolute;left:0;top:181px;width:100%;height:24px;background:var(--bar);opacity:.95}
.nav__item{position:absolute;top:5px;font-size:7px;letter-spacing:.5px;color:var(--nav-text)}
.nav__item--active{left:480px;top:2px;width:53px;height:16px;line-height:16px;text-align:center;background:var(--tab);color:var(--tab-text)}
.nav__item--blog{left:550px}

.teaser{position:absolute;width:160px;font-size:7px;line-height:9.6px}
.teaser h2,.gallery h2{font-weight:400;font-size:11px;color:var(--heading);margin-bottom:4px}
.teaser--reporting{left:17px;top:216px}
.teaser--about{left:187px;top:216px}
.teaser p{height:70px}
.btn{display:inline-block;background:var(--button);color:var(--button-text);font-size:6.5px;padding:2px 9px;border-radius:2px;margin-top:4px}
.teaser .btn{padding:2px 10px}
.col-divider{position:absolute;left:180px;top:212px;width:1px;height:232px;background:var(--rule)}
.row-divider{position:absolute;left:12px;top:322px;width:345px;height:1px;background:var(--rule)}
.gallery{position:absolute;top:329px;width:152px}
.gallery--clients{left:19px}
.gallery--methods{left:189px}
.gallery__photo{width:152px;height:110px;background:linear-gradient(180deg,#a9cdea 0%,#d9e6ee 38%,#6a8aa8 55%,#2f5a86 70%,#173a63 100%)}

.contact{position:absolute;left:357px;top:205px;width:117px;height:239px;background:var(--mid);padding:8px 9px;font-size:6.5px}
.contact__lead{margin-bottom:10px}
.field{height:11px;background:var(--field);border:1px solid var(--field-line);font-size:6px;padding-left:3px;line-height:9px;margin-bottom:4px}
.contact__check,.contact__radio{display:flex;align-items:center;gap:3px;margin-bottom:4px}
.box{display:inline-block;width:6px;height:6px;border:1px solid var(--field-line);background:var(--field)}

.sidebar{position:absolute;left:474px;top:205px;width:118px;height:239px;background:var(--side);border-left:1px solid var(--rule);padding:12px 10px 0 10px;font-size:6.5px}
.sidebar__search{height:11px;width:95px;background:var(--search);border:1px solid var(--field-line);margin-bottom:10px}
.login label{display:block;font-size:6.5px;margin-bottom:1px;padding-left:6px}
.login .field{width:85px;margin-left:6px}
.login .contact__check{padding-left:6px}
.login .btn{margin:0 0 8px 6px;padding:2px 9px}
.links{list-style:none;padding-left:6px}
.links li{line-height:12px;color:var(--link);text-decoration:underline}
.links li::before{content:"";display:inline-block;width:3px;height:3px;background:var(--link);margin-right:4px;vertical-align:middle}
.links--account{margin-bottom:6px}
</style>
</head>
<body>

<section class="palette palette--blue theme-blue">
  <header class="masthead" role="img" aria-label="Soft blue backdrop of light squares behind a photo of four colleagues gathered around a laptop">
    <div class="masthead__photo"></div>
  </header>
  <div class="brand"><span class="brand__mark"></span>Wellvane</div>
  <div class="masthead__search"></div>
  <nav class="nav"><span class="nav__item nav__item--active">HOME</span><span class="nav__item nav__item--blog">BLOG</span></nav>
  <article class="teaser teaser--reporting"><h2>Reporting</h2><p>Maecenas auctor interdum id ut non faucibus quis et a et aenean venenatis auctor pede eu etiam etiam sapien. Metus libero duis eget ante turpis quis orci blandit mollis in nunc magna ligula. Quis tortor phasellus rutrum.</p><span class="btn">More Info</span></article>
  <article class="teaser teaser--about"><h2>About Us</h2><p>Tortor quis eros nisl maecenas lacus elit mauris ultrices ut suscipit accumsan porta consequat phasellus mi. Fusce ac aenean dolor et fames leo orci posuere nunc sodales ut in vestibulum. Phasellus nulla fermentum..</p><span class="btn">More Info</span></article>
  <div class="col-divider"></div><div class="row-divider"></div>
  <figure class="gallery gallery--clients"><h2>Clients</h2><div class="gallery__photo" role="img" aria-label="Photo of a snowy mountain above a still lake"></div></figure>
  <figure class="gallery gallery--methods"><h2>New Methods</h2><div class="gallery__photo" role="img" aria-label="Photo of a misty lake at dawn"></div></figure>
  <aside class="contact"><p class="contact__lead">Enter content here...</p><div class="field">Text...</div><div class="contact__check"><span class="box"></span>Lorem ipsum dolor.</div><div class="contact__radio"><span class="box"></span>Text... <span class="box"></span>Text...</div><span class="btn">Send</span></aside>
  <aside class="sidebar"><div class="sidebar__search"></div><form class="login"><label>Username</label><div class="field"></div><label>Password</label><div class="field"></div><div class="contact__check"><span class="box"></span>Remember Me</div><span class="btn">Login</span></form>
    <ul class="links links--account"><li>Forgot your password?</li><li>Forgot your username?</li><li>Create an account</li></ul>
    <ul class="links"><li>My first blog</li><li>Who will prevail?</li><li>Stay positive!</li><li>Oil still going up</li><li>Gripes and Grins</li><li>2012 Olympics</li><li>How to SEO</li><li>On Global Warming</li></ul></aside>
</section>

<section class="palette palette--grey theme-grey">
  <header class="masthead" role="img" aria-label="Pale grey-green backdrop of light squares behind a photo of four colleagues gathered around a laptop">
    <div class="masthead__photo"></div>
  </header>
  <div class="brand"><span class="brand__mark"></span>Wellvane</div>
  <div class="masthead__search"></div>
  <nav class="nav"><span class="nav__item nav__item--active">HOME</span><span class="nav__item nav__item--blog">BLOG</span></nav>
  <article class="teaser teaser--reporting"><h2>Reporting</h2><p>Maecenas auctor interdum id ut non faucibus quis et a et aenean venenatis auctor pede eu etiam etiam sapien. Metus libero duis eget ante turpis quis orci blandit mollis in nunc magna ligula. Quis tortor phasellus rutrum.</p><span class="btn">More Info</span></article>
  <article class="teaser teaser--about"><h2>About Us</h2><p>Tortor quis eros nisl maecenas lacus elit mauris ultrices ut suscipit accumsan porta consequat phasellus mi. Fusce ac aenean dolor et fames leo orci posuere nunc sodales ut in vestibulum. Phasellus nulla fermentum..</p><span class="btn">More Info</span></article>
  <div class="col-divider"></div><div class="row-divider"></div>
  <figure class="gallery gallery--clients"><h2>Clients</h2><div class="gallery__photo" role="img" aria-label="Photo of a snowy mountain above a still lake"></div></figure>
  <figure class="gallery gallery--methods"><h2>New Methods</h2><div class="gallery__photo" role="img" aria-label="Photo of a misty lake at dawn"></div></figure>
  <aside class="contact"><p class="contact__lead">Enter content here...</p><div class="field">Text...</div><div class="contact__check"><span class="box"></span>Lorem ipsum dolor.</div><div class="contact__radio"><span class="box"></span>Text... <span class="box"></span>Text...</div><span class="btn">Send</span></aside>
  <aside class="sidebar"><div class="sidebar__search"></div><form class="login"><label>Username</label><div class="field"></div><label>Password</label><div class="field"></div><div class="contact__check"><span class="box"></span>Remember Me</div><span class="btn">Login</span></form>
    <ul class="links links--account"><li>Forgot your password?</li><li>Forgot your username?</li><li>Create an account</li></ul>
    <ul class="links"><li>My first blog</li><li>Who will prevail?</li><li>Stay positive!</li><li>Oil still going up</li><li>Gripes and Grins</li><li>2012 Olympics</li><li>How to SEO</li><li>On Global Warming</li></ul></aside>
</section>

<section class="palette palette--green theme-green">
  <header class="masthead" role="img" aria-label="Soft green backdrop of light squares behind a photo of four colleagues gathered around a laptop">
    <div class="masthead__photo"></div>
  </header>
  <div class="brand"><span class="brand__mark"></span>Wellvane</div>
  <div class="masthead__search"></div>
  <nav class="nav"><span class="nav__item nav__item--active">HOME</span><span class="nav__item nav__item--blog">BLOG</span></nav>
  <article class="teaser teaser--reporting"><h2>Reporting</h2><p>Maecenas auctor interdum id ut non faucibus quis et a et aenean venenatis auctor pede eu etiam etiam sapien. Metus libero duis eget ante turpis quis orci blandit mollis in nunc magna ligula. Quis tortor phasellus rutrum.</p><span class="btn">More Info</span></article>
  <article class="teaser teaser--about"><h2>About Us</h2><p>Tortor quis eros nisl maecenas lacus elit mauris ultrices ut suscipit accumsan porta consequat phasellus mi. Fusce ac aenean dolor et fames leo orci posuere nunc sodales ut in vestibulum. Phasellus nulla fermentum..</p><span class="btn">More Info</span></article>
  <div class="col-divider"></div><div class="row-divider"></div>
  <figure class="gallery gallery--clients"><h2>Clients</h2><div class="gallery__photo" role="img" aria-label="Photo of a snowy mountain above a still lake"></div></figure>
  <figure class="gallery gallery--methods"><h2>New Methods</h2><div class="gallery__photo" role="img" aria-label="Photo of a misty lake at dawn"></div></figure>
  <aside class="contact"><p class="contact__lead">Enter content here...</p><div class="field">Text...</div><div class="contact__check"><span class="box"></span>Lorem ipsum dolor.</div><div class="contact__radio"><span class="box"></span>Text... <span class="box"></span>Text...</div><span class="btn">Send</span></aside>
  <aside class="sidebar"><div class="sidebar__search"></div><form class="login"><label>Username</label><div class="field"></div><label>Password</label><div class="field"></div><div class="contact__check"><span class="box"></span>Remember Me</div><span class="btn">Login</span></form>
    <ul class="links links--account"><li>Forgot your password?</li><li>Forgot your username?</li><li>Create an account</li></ul>
    <ul class="links"><li>My first blog</li><li>Who will prevail?</li><li>Stay positive!</li><li>Oil still going up</li><li>Gripes and Grins</li><li>2012 Olympics</li><li>How to SEO</li><li>On Global Warming</li></ul></aside>
</section>

</body>
</html>
```